Unique business card design

Boutique coastal hotel suites - in need of clever stand out business card I have uploaded the logo that I had created through quill forge I want something that is clever and stands out from everyone else - 418 Brantwell Avenue seldovia Alaska 99571 phone or text 907 -581-6142 www.primemarrowbysuites.com

Target Market(s)

Men and woman

Industry/Entity Type

Boutique coastal hotel

Contact Information for Business Card

Marrowby Suites Kelbrook Alaska marrowby_suites@mailnest.net

Requirements
Must have
• Classy - clever -bold 907-581-6142 call or text

```html
<!DOCTYPE html>
<html lang="en">
<head>
<meta charset="utf-8">
<title>Marrowby Suites — Business Card</title>
<link rel="stylesheet" href="https://fonts.googleapis.com/css2?family=Montserrat:wght@400;600&display=swap">
<style>
  :root {
    --backdrop: #e4e4e4;
    --card-front: #ffffff;
    --card-back: #ece9e2;
    --logo-panel: #ece9e2;
    --navy: #2c4a6b;
    --ink: #4a4a4a;
    --rule: #111111;
  }
  * { box-sizing: border-box; margin: 0; padding: 0; }
  html, body {
    width: 1133px; height: 1200px; overflow: hidden;
    background: var(--backdrop);
    font-family: "Montserrat", sans-serif;
  }
  .canvas { position: relative; width: 1133px; height: 1200px; }

  .card {
    position: absolute; left: 215px; width: 702px; height: 400px;
  }
  .card--front { top: 151px; background: var(--card-front); }
  .card--back  { top: 647px; background: var(--card-back); border-bottom: 4px solid var(--rule); }

  .brand-panel {
    position: absolute; left: 169px; top: 130px; width: 365px; height: 142px;
    background: var(--logo-panel);
    border-bottom: 4px solid var(--rule);
    display: flex; align-items: center; justify-content: center;
  }
  .brand-name {
    font-weight: 600; color: var(--navy);
    text-transform: uppercase; letter-spacing: 0.08em;
    font-size: 29px; white-space: nowrap;
  }

  .brand-lockup {
    position: absolute; left: 225px; top: 70px; width: 253px; height: 88px;
    border-bottom: 2px solid var(--rule);
    display: flex; align-items: center; justify-content: center;
  }
  .brand-lockup .brand-name { font-size: 21px; }

  .contact {
    position: absolute; left: 0; width: 100%;
    text-align: center; color: var(--ink); font-style: normal;
    font-size: 15px; letter-spacing: 0.06em; line-height: 21px;
  }
  .contact--address { top: 193px; }
  .contact--reach { top: 292px; }
  .icon-row { display: flex; justify-content: center; gap: 9px; margin-bottom: 7px; }
  .icon { width: 16px; height: 16px; fill: var(--navy); }
</style>
</head>
<body>
<main class="canvas">
  <section class="card card--front">
    <div class="brand-panel">
      <span class="brand-name">Marrowby Suites</span>
    </div>
  </section>

  <section class="card card--back">
    <div class="brand-lockup">
      <span class="brand-name">Marrowby Suites</span>
    </div>

    <address class="contact contact--address">
      <div class="icon-row">
        <svg class="icon" viewBox="0 0 16 16" aria-hidden="true"><path d="M8 1 0.5 7.5l1 1.1L3 7.3V15h4v-4h2v4h4V7.3l1.5 1.3 1-1.1L12 4.6V2h-2v1L8 1z"/></svg>
      </div>
      418 Brantwell Avenue kelbrook<br>Alaska 99571
    </address>

    <div class="contact contact--reach">
      <div class="icon-row">
        <svg class="icon" viewBox="0 0 16 16" aria-hidden="true"><path d="M3.5 1.5 6 4 4.7 5.6c.8 2 2.4 3.6 4.4 4.5L10.8 9l2.6 2.5-1.4 2.3c-5.2-.5-9.4-4.8-9.8-10l1.3-2.3zM9 1.5a5.5 5.5 0 0 1 5.5 5.5h-1.3A4.2 4.2 0 0 0 9 2.8V1.5zm0 2.6A2.9 2.9 0 0 1 11.9 7h-1.3A1.6 1.6 0 0 0 9 5.4V4.1z"/></svg>
        <svg class="icon" viewBox="0 0 16 16" aria-hidden="true"><path d="M1 2h14v12H1V2zm2 2v8h10V4l-5 4-5-4z"/></svg>
        <svg class="icon" viewBox="0 0 16 16" aria-hidden="true"><path d="M8 1a7 7 0 1 0 0 14A7 7 0 0 0 8 1zm-.6 1.4v2.8H5.3c.5-1.5 1.2-2.5 2.1-2.8zm1.2 0c.9.3 1.6 1.3 2.1 2.8H8.6V2.4zM4 5.2H2.9a5.7 5.7 0 0 1 2.5-2.3A7 7 0 0 0 4 5.2zm8 0a7 7 0 0 0-1.4-2.3 5.7 5.7 0 0 1 2.5 2.3H12zM2.4 6.4h1.4a10 10 0 0 0 0 3.2H2.4a5.7 5.7 0 0 1 0-3.2zm2.6 0h2.4v3.2H5a8.5 8.5 0 0 1 0-3.2zm3.6 0H11a8.5 8.5 0 0 1 0 3.2H8.6V6.4zm3.6 0h1.4a5.7 5.7 0 0 1 0 3.2h-1.4a10 10 0 0 0 0-3.2zM2.9 10.8H4a7 7 0 0 0 1.4 2.3 5.7 5.7 0 0 1-2.5-2.3zm2.4 0h2.1v2.8c-.9-.3-1.6-1.3-2.1-2.8zm3.3 0h2.1c-.5 1.5-1.2 2.5-2.1 2.8v-2.8zm3.4 0h1.1a5.7 5.7 0 0 1-2.5 2.3 7 7 0 0 0 1.4-2.3z"/></svg>
      </div>
      907-581-6142<br>
      marrowby_suites@mailnest.net<br>
      www.primemarrowbysuites.com
    </div>
  </section>
</main>
</body>
</html>
```